Bright, Bold Sydney Tutoring Business Flyer Advertisment

Brightpath is an up and coming tutoring business located on Sydney's Upper North Shore catering to school students of all ages. We need a flyer designed for notice boards and letter box drops to attract new clients. Our tutors are mostly university education students who are fresh, dedicated and passionate about their areas of teaching. The flyer should exhibit a bright, bold, modern, clean cut style which would appeal to both students and parents. I have attached our logo (the flyer could reflect this colour scheme), and a PDF which outlines the information we would like to appear on the flyer. This is not set in stone, but designed to act as an extremely loose guide for your creativity !

Target Market(s)

Affluent School Students and Parents

Industry/Entity Type

Tutoring

Requirements
Must have
• Logo, $10 offer, company description.
Nice to have
• Grabbing headlines to attract new clients, such as "Feeling overwhelmed at school?". We are looking for an eye catching, clean cut and professional design that has the colours to attract kids and the tone to attract parents.

```html
<!DOCTYPE html>
<html lang="en">
<head>
<meta charset="utf-8">
<title>Brightpath Tutoring Flyer</title>
<link rel="stylesheet" href="https://fonts.googleapis.com/css2?family=Roboto+Condensed:ital,wght@0,300;0,400;0,700;1,700&family=Lato:wght@400;700&display=swap">
<style>
  :root {
    --pink: #e8608e;
    --pink-light: #f4a9c4;
    --crimson: #cf1f5a;
    --blue: #1d4fa0;
    --blue-bright: #2d68c6;
    --blue-pale: #b9d3f2;
    --ink: #3a3a3a;
    --paper-top: #ffffff;
    --paper-bottom: #e9e9eb;
    --white: #ffffff;
  }
  * { margin: 0; padding: 0; box-sizing: border-box; }
  html, body { width: 902px; height: 1200px; overflow: hidden; }
  body { background: var(--paper-bottom); font-family: "Roboto Condensed", Arial, sans-serif; }

  .flyer {
    position: relative; width: 902px; height: 1200px; overflow: hidden;
    background: linear-gradient(180deg, var(--paper-top) 0%, #f6f6f7 55%, var(--paper-bottom) 100%);
  }

  .brand {
    position: absolute; left: 34px; top: 120px; width: 200px;
    display: flex; align-items: center; gap: 10px;
  }
  .brand-dot { width: 22px; height: 22px; border-radius: 50%; background: var(--pink); flex: none; }
  .brand-name { font-family: "Lato", sans-serif; font-weight: 700; font-size: 34px; color: #2b2b2b; }

  .hero-ring {
    position: absolute; left: 213px; top: 26px; width: 700px; height: 700px;
    border-radius: 50%; border: 16px solid var(--blue-bright);
    box-shadow: inset 0 0 0 8px var(--blue-pale);
  }
  .hero-photo {
    position: absolute; left: 237px; top: 50px; width: 652px; height: 652px; border-radius: 50%;
    background:
      radial-gradient(ellipse 34% 26% at 50% 48%, #2a3f8f 0%, #2f4796 70%, rgba(47,71,150,0) 100%),
      linear-gradient(160deg, #efeeec 0%, #d9d6d2 45%, #c9c5c0 100%);
  }

  .offer {
    position: absolute; left: 70px; top: 268px; width: 336px; height: 336px; border-radius: 50%;
    border: 8px solid var(--white);
    background: radial-gradient(circle at 40% 60%, #f7c4d7 0%, #ef86aa 45%, var(--pink) 100%);
    color: var(--white); text-align: center; font-family: "Lato", sans-serif;
    display: flex; flex-direction: column; justify-content: center;
  }
  .offer-lead { font-size: 28px; line-height: 1.18; font-weight: 400; }
  .offer-price { font-size: 84px; font-weight: 700; line-height: 1; margin-top: 6px; }

  .intro { position: absolute; left: 44px; top: 758px; width: 380px; color: var(--ink); }
  .intro-title { font-weight: 700; font-size: 44px; line-height: 1; letter-spacing: -0.5px; }
  .intro-title .accent { color: var(--crimson); }
  .intro-title .tail { color: var(--blue-bright); }
  .intro-lead { font-weight: 300; font-size: 26px; line-height: 1.2; margin-top: 10px; }
  .intro-note { font-weight: 400; font-size: 17px; line-height: 1.25; margin-top: 16px; }

  .contact-card {
    position: absolute; left: 44px; top: 1018px; width: 360px; height: 158px;
    background: var(--white); border-radius: 12px 12px 0 0;
    box-shadow: 0 0 10px rgba(0,0,0,0.18); padding: 16px 18px 0; z-index: 2;
  }
  .contact-item {
    display: flex; align-items: flex-start; gap: 12px; margin-bottom: 9px;
    font-style: italic; font-weight: 700; font-size: 20px; color: var(--crimson); line-height: 1.2;
  }
  .contact-item svg { flex: none; margin-top: 4px; fill: var(--blue); }

  .prompt {
    position: absolute; left: 440px; width: 462px; height: 84px; padding-right: 40px;
    display: flex; align-items: center; justify-content: flex-end; text-align: right;
    color: var(--white); font-weight: 700; line-height: 1.12;
  }
  .prompt-stress { top: 770px; font-size: 31px; background: linear-gradient(90deg, var(--pink-light) 0%, var(--pink) 45%, var(--pink) 100%); }
  .prompt-skills { top: 872px; font-size: 26px; background: linear-gradient(90deg, #ffffff 0%, var(--blue-bright) 28%, var(--blue) 100%); }
  .prompt-engage { top: 968px; font-size: 26px; background: linear-gradient(90deg, var(--pink-light) 0%, var(--pink) 45%, var(--pink) 100%); }

  .call { position: absolute; right: 40px; top: 1064px; text-align: right; }
  .call-title { font-weight: 700; font-size: 32px; color: var(--blue); }
  .call-text { font-family: "Lato", sans-serif; font-weight: 700; font-size: 19px; color: #4a4a4a; line-height: 1.35; margin-top: 4px; }

  .base-band {
    position: absolute; left: 0; bottom: 0; width: 902px; height: 24px; z-index: 1;
    background: linear-gradient(90deg, #6c8fcc 0%, var(--blue) 50%, #173f84 100%);
  }
</style>
</head>
<body>
<main class="flyer">
  <div class="brand">
    <span class="brand-dot"></span>
    <span class="brand-name">brightpath</span>
  </div>

  <div class="hero-ring"></div>
  <div class="hero-photo" role="img" aria-label="Close-up photo of a keyboard with a blue Education key showing a graduation cap"></div>

  <section class="offer">
    <p class="offer-lead">Mention<br>this advertisement<br>to claim your trial<br>session for just</p>
    <p class="offer-price">$10!</p>
  </section>

  <section class="intro">
    <h1 class="intro-title"><span class="accent">Brightpath</span> <span class="tail">Tutoring</span></h1>
    <p class="intro-lead">offers one-on-one, individualised<br>learning experiences to maximise<br>academic development.</p>
    <p class="intro-note">Our tutors are hand selected on the basis of<br>their qualifications, expertise and passion<br>for inspiring young learners.</p>
  </section>

  <address class="contact-card">
    <div class="contact-item">
      <svg width="16" height="12" viewBox="0 0 16 12"><path d="M0 0h16v12H0z" opacity=".9"/><path d="M0 0l8 6 8-6" fill="none" stroke="#fff" stroke-width="1.5"/></svg>
      <span>info@brightpathtutoring.com.au</span>
    </div>
    <div class="contact-item">
      <svg width="16" height="16" viewBox="0 0 16 16"><circle cx="8" cy="8" r="7.5"/><path d="M1 8h14M8 1c-3 3.5-3 10.5 0 14M8 1c3 3.5 3 10.5 0 14" fill="none" stroke="#fff" stroke-width="1.2"/></svg>
      <span>www.brightpathtutoring.com.au</span>
    </div>
    <div class="contact-item">
      <svg width="16" height="15" viewBox="0 0 16 15"><path d="M8 0L0 7h2v8h4v-5h4v5h4V7h2z"/></svg>
      <span>Suite 4, 220 Ridge Road<br>Kellham, NSW 2075</span>
    </div>
  </address>

  <p class="prompt prompt-stress">Feeling overwhelmed by<br>the HSC?</p>
  <p class="prompt prompt-skills">Looking to improve your skills,<br>confidence and organisation?</p>
  <p class="prompt prompt-engage">Want to increase your child’s<br>engagement at school?</p>

  <section class="call">
    <h2 class="call-title">Contact us today!!</h2>
    <p class="call-text">to discuss how we can help make your<br>learning goals a reality</p>
  </section>

  <div class="base-band"></div>
</main>
</body>
</html>
```